Quelindra - Step Into Bloom! Business Card

We are bringing an amazing new system of dance to Australia and need a nifty, eye-catching little card that we can give to everyone to get them to come to class.

It needs a bit of information about Quelindra, along with contact details and a space for us to write a note for people about the next class.

Target Market(s)

30+ people that enjoy dance and are interested in self-development, meeting people and getting more out of life.

Industry/Entity Type

Business

Requirements
Must have
• Double sided in colour

A beautiful, simple design that indicates movement and is modern, fresh and uplifting.

The attached Quelindra logo

Text for the front :

Quelindra - the Step Into Bloom

Dance from your heart and feel your life open.

Regular classes in Sydney and Canberra with Maren Hollis and Ernesto Varga

Text for the back :

Quelindra ignites our vital spark for life and awakens our innate potential for pleasurable, joyful, heartfelt living through dance, music and authentic connection.

Ernesto and Maren are committed to offering authentic, supportive and inspiring spaces for your growth through Quelindra.

Contact us on maren@quelindra.com.au - evtrusk@zentromail.net or 0472 318 904.

www.quelindra.com.au

Nice to have
• Some movement in the design

Use some of the photos attached in some form - could be faded, incorporated into design etc.

Creative use of the logo - integrating it within the design - e.g perhaps using it as the O in Quelindra,
Should not have
• Not a lot of black

```html
<!DOCTYPE html>
<html lang="en">
<head>
<meta charset="utf-8">
<title>Quelindra – Step Into Bloom business card</title>
<link rel="stylesheet" href="https://fonts.googleapis.com/css2?family=Cinzel:wght@400;700&family=Poiret+One&display=swap">
<style>
  :root {
    --page-bg: #e9e9ec;
    --plum: #8e1f63;
    --plum-deep: #74134f;
    --plum-light: #b24a92;
    --blush: #f3c8e2;
    --ink: #2a1422;
    --lime: #dfe84a;
    --petal: #f6dcea;
    --shadow: rgba(40, 20, 35, 0.28);
  }
  * { margin: 0; padding: 0; box-sizing: border-box; }
  html, body {
    width: 1200px; height: 997px; overflow: hidden;
    background: var(--page-bg);
  }
  .stage { position: relative; width: 1200px; height: 997px; }

  .card {
    position: absolute;
    width: 760px; height: 440px;
    border-radius: 26px;
    box-shadow: 0 10px 28px var(--shadow);
    overflow: hidden;
  }

  /* ---------- back side ---------- */
  .card-back {
    left: 80px; top: 36px;
    background: var(--blush);
    color: var(--ink);
    font-family: "Cinzel", serif;
    text-align: center;
  }
  .back-header {
    display: flex; align-items: center; gap: 28px;
    padding: 30px 40px 0 40px;
  }
  .mark-small {
    display: flex; align-items: center; justify-content: center;
    width: 96px; height: 96px;
    border-radius: 50%;
    border: 1.5px solid var(--plum);
    font-size: 13px; color: var(--plum);
    flex: none;
  }
  .back-title {
    font-family: "Poiret One", sans-serif;
    font-weight: 400;
    font-size: 36px; color: var(--plum);
    letter-spacing: 1px;
  }
  .back-title .brand { letter-spacing: 2px; }
  .back-body { padding: 8px 70px 0; font-size: 17.5px; line-height: 1.45; }
  .back-body p { margin-bottom: 20px; }
  .back-web { font-weight: 700; font-size: 18px; letter-spacing: 1px; margin-top: -4px; }

  /* ---------- front side ---------- */
  .card-front {
    left: 360px; top: 520px;
    background: radial-gradient(ellipse at 50% 32%, var(--plum-light) 0%, var(--plum) 45%, var(--plum-deep) 100%);
    color: var(--petal);
    font-family: "Cinzel", serif;
  }
  .photo {
    position: absolute;
    width: 176px; height: 176px;
    border-radius: 50%;
    border: 4px solid var(--plum-deep);
  }
  .photo-left {
    left: 44px; top: 66px;
    background: radial-gradient(circle at 45% 40%, #d8cfc6 0%, #a88a78 55%, #6a4a3e 100%);
  }
  .photo-right {
    right: 40px; top: 22px;
    background: radial-gradient(circle at 50% 45%, #eeeae6 0%, #9c7a72 50%, #4a3036 100%);
  }
  .mark-large {
    position: absolute; left: 50%; top: 26px;
    transform: translateX(-50%);
    width: 180px; height: 180px;
    border-radius: 50%;
    border: 2px dotted var(--petal);
    display: flex; align-items: center; justify-content: center;
    font-size: 22px; color: var(--petal);
    letter-spacing: 1px;
  }
  .front-title {
    position: absolute; left: 0; right: 0; top: 258px;
    text-align: center;
    font-family: "Poiret One", sans-serif;
    font-weight: 400;
    color: var(--lime);
    font-size: 44px; line-height: 1.1;
    white-space: nowrap;
  }
  .front-title .brand { font-size: 50px; letter-spacing: 2px; }
  .front-tagline {
    position: absolute; left: 0; right: 0; bottom: 30px;
    text-align: center;
    font-size: 20px; line-height: 1.3;
    padding: 0 60px;
  }
</style>
</head>
<body>
<main class="stage">

  <section class="card card-back" aria-label="Card back">
    <header class="back-header">
      <div class="mark-small">Quelindra</div>
      <h2 class="back-title"><span class="brand">QUELINDRA</span> - the Step Into Bloom</h2>
    </header>
    <div class="back-body">
      <p>Quelindra ignites our vital spark for life and awakens our innate potential for pleasurable, joyful, heartfelt living through dance, music and authentic connection.</p>
      <p>Ernesto and Maren are committed to offering authentic, supportive and inspiring spaces for your growth through Quelindra.</p>
      <p>Contact us on maren@quelindra.com.au - evtrusk@zentromail.net or 0472 318 904.</p>
      <p class="back-web">www.quelindra.com.au</p>
    </div>
  </section>

  <section class="card card-front" aria-label="Card front">
    <div class="photo photo-left" role="img" aria-label="Photo of a couple dancing with raised arms"></div>
    <div class="mark-large">Quelindra</div>
    <div class="photo photo-right" role="img" aria-label="Photo of two dancers holding hands in class"></div>
    <h1 class="front-title"><span class="brand">QUELINDRA</span> - the Step Into Bloom</h1>
    <p class="front-tagline">Dance from your heart and feel your life open.<br>Regular classes in Sydney and Canberra with<br>Maren Hollis and Ernesto Varga</p>
  </section>

</main>
</body>
</html>
```